Flyer für eine Immobilienverwaltung
Zielgruppe
ich bitte die Dienste einer Immobilienverwaltung an sowie die Versicherungen und Finanzierungen dieser (siehe auch dem angehängten Flyer)
Zielgruppe sind Investoren, Eigentümer (keine WEG Verwaltung) die einen Rundum Service möchten.
Aufgabenstellung
Unser Konzept: Wenige Objekte, Intensive Betreuung
Unser Fokus: Ertrag & Entwicklung
Unsere Vision ist es, durch intensive, ganzheitliche Betreuung und strategisches Life-Cycle-Management die nachhaltige Ertragsstärke Ihrer Liegenschaft zu sichern und ihren Wert zukunftsweisend zu steigern.
Zusätzlich sollen hervorgehoben werden das es ein Rundumservice von vor Vertragsabschluss bis zum Sanierungs und Renovierungsmanagement geht.
Ich habe den Inhalt des Flyers beigefügt (gerne noch Änderungen oder Vorschläge)
Ebenfalls würde ich gerne ein Bild haben, welches dem angehängten sehr ähnelt.
Update
Leider habe ich noch kein Logo. ich würde gerne eins haben mit einem ähnlichen Bild wie ich angehängt habe, in dem man die Immobilien sieht, zusammen mit dem Namen: Haven Crest Property Stewardship. Farbwahl bin ich offen. Es ist aufgefallen, dass die Kontaktdaten fehlen. Diese sind hier.
Jonas Trewelt
Info@wohnwerk-jt.de
Mobil: +49 1573 42 19 605
Am Lindenhang 7, 74921 Hohenweiler
Update:
Ich habe noch Bild von mir angefügt, das zu den Kontaktdaten kommen soll.

```html
<!DOCTYPE html>
<html lang="de">
<head>
<meta charset="utf-8">
<title>Haven Crest Property Stewardship – Flyer</title>
<link href="https://fonts.googleapis.com/css2?family=Roboto+Slab:wght@600;700&family=Open+Sans:wght@400;600;700&display=swap" rel="stylesheet">
<style>
:root{
  --stage:#dadada;
  --paper:#ffffff;
  --slate:#aebcc5;
  --ink:#2e3a42;
  --ink-soft:#3d4a52;
  --title-block:#3a4852;
  --contact:#4a5660;
  --photo-light:#cfd8de;
  --photo-dark:#27323a;
}
*{margin:0;padding:0;box-sizing:border-box}
html,body{width:677px;height:1200px;overflow:hidden}
body{background:var(--stage);font-family:"Open Sans",Arial,sans-serif;color:var(--ink);position:relative}
.spread{position:absolute;left:18px;width:640px;height:340px;display:flex;box-shadow:0 3px 8px rgba(0,0,0,.35)}
.spread--outside{top:250px}
.spread--inside{top:620px}
.panel{width:160px;height:100%;position:relative;padding:16px 11px 0 13px;font-size:4.5px;line-height:6.1px;overflow:hidden}
.panel--slate{background:var(--slate)}
.panel--paper{background:var(--paper)}
h2{font-family:"Roboto Slab",Georgia,serif;font-weight:600;font-size:7.2px;line-height:8.4px;margin-bottom:3px;color:var(--ink)}
h3{font-family:"Roboto Slab",Georgia,serif;font-weight:600;font-size:5.3px;line-height:6.5px;margin:4px 0 1px}
h4{font-weight:700;font-size:4.6px;line-height:6px;margin-top:3px}
p{margin:0}
ol,ul{list-style:none}
ol li{padding-left:7px;position:relative}
ol li::before{content:attr(data-n);position:absolute;left:0}
ul li{padding-left:7px;position:relative}
ul li::before{content:"•";position:absolute;left:1px}
.fine{font-size:4.1px;line-height:5.5px}
.fine h3{font-size:4.9px;margin-top:3px}
.fine ul li::before{font-size:3.5px}
b{font-weight:700}
.gap{height:5px}
.contact{position:absolute;left:37px;top:297px;width:85px;height:38px;background:var(--contact);color:#e9eef1;padding:4px 5px;font-size:4.3px;line-height:5.6px}
.contact b{color:#fff}
.cover{padding:0;background:var(--paper)}
.cover__title{position:absolute;left:13px;top:32px}
.cover__title span{display:table;background:var(--title-block);color:#fff;font-family:"Roboto Slab",Georgia,serif;font-weight:700;font-size:13.5px;line-height:17px;padding:0 4px;margin-bottom:1px}
.cover__photo{position:absolute;left:0;top:0;width:160px;height:340px}
</style>
</head>
<body>

<section class="spread spread--outside">
  <div class="panel panel--slate">
    <ol>
      <li data-n="">der Neuvermietung von Wohnungen werden mit einer Provision von [z. B. 2 Monatskaltmieten] vom Vermieter (Bestellerprinzip) vergütet.</li>
      <li data-n="3.">Sonderleistungen (z. B. Modernisierungsbetreuung, Versicherungsfälle, Eigentümerversammlungen außerhalb der üblichen Turnusse, Mahnverfahren etc.) werden mit [z. B. 80–120 € netto pro Stunde] oder nach gesonderter Vereinbarung / Pauschale abgerechnet.</li>
      <li data-n="4.">Alle Honorare verstehen sich zzgl. der zum Zeitpunkt der Rechnungstellung gültigen gesetzlichen Mehrwertsteuer.</li>
    </ol>
    <h3>§ 4 Vertragsdauer und Kündigung</h3>
    <ol>
      <li data-n="1.">Der Vertrag beginnt am [Datum] und läuft unbefristet.</li>
      <li data-n="2.">Die ordentliche Kündigung ist mit einer Frist von [z. B. 3 Monaten] zum Monatsende für beide Parteien möglich.</li>
      <li data-n="3.">Das Recht zur außerordentlichen fristlosen Kündigung aus wichtigem Grund bleibt unberührt.</li>
      <li data-n="4.">Die Kündigung bedarf der Schriftform.</li>
    </ol>
    <h3>§ 5 Haftung</h3>
    <ol>
      <li data-n="1.">Der Verwalter haftet für die ordnungsgemäße Durchführung der vertraglich geschuldeten Leistungen im Rahmen der gesetzlichen Vorschriften.</li>
      <li data-n="2.">Für Tätigkeiten Dritter (z. B. Handwerker, Bauunternehmen) haftet der Verwalter nicht, es sei denn, ihm ist grobe Fahrlässigkeit oder Vorsatz bei der Auswahl / Vermittlung nachzuweisen.</li>
      <li data-n="3.">Die Haftung für einfache Fahrlässigkeit wird auf den typischerweise vorhersehbaren Schaden beschränkt.</li>
    </ol>
    <h3>§ 6 Schlussbestimmungen</h3>
    <ol>
      <li data-n="1.">Änderungen und Ergänzungen dieses Vertrages bedürfen der Schriftform.</li>
      <li data-n="2.">Sollten einzelne Bestimmungen dieses Vertrags unwirksam sein / werden, bleibt der Vertrag im Übrigen wirksam. Die Parteien verpflichten sich, die unwirksame durch eine wirksame Regelung zu ersetzen, die dem wirtschaftlich Gewollten möglichst nahekommt.</li>
    </ol>
    <div class="gap"></div>
    <p>[Ort, Datum, Unterschriften Auftraggeber und Verwalter]</p>
    <h3>Anlage:</h3>
    <p>Leistungsverzeichnis / Leistungsprofil (vollständig detailliert, wie oben formuliert)</p>
  </div>

  <div class="panel panel--paper fine">
    <h2>Datenschutzerklärung<br>(Muster Haus- / Mietverwaltung)</h2>
    <h4>Datenschutzerklärung gemäß DSGVO</h4>
    <p>Wir, [Name und Anschrift der Verwaltung], nehmen den Schutz Ihrer personenbezogenen Daten sehr ernst und behandeln Ihre Daten vertraulich sowie gemäß den gesetzlichen Datenschutzvorschriften (insbesondere DSGVO) und dieser Datenschutzerklärung.</p>
    <h3>1. Verantwortlicher und Datenschutzbeauftragter</h3>
    <p>Verantwortlicher ist:<br>[Name, Adresse, E-Mail, Telefon]<br>Optional: Datenschutzbeauftragter (Kontakt)</p>
    <h3>2. Art der verarbeiteten Daten</h3>
    <p>Wir verarbeiten insbesondere folgende personenbezogene Daten:</p>
    <ul>
      <li>Name, Anschrift, Telefonnummer, E-Mail-Adresse</li>
      <li>Geburtsdatum</li>
      <li>Bankverbindung</li>
      <li>Vertragsdaten (Miet- / Eigentumsverhältnis)</li>
      <li>Zahlungsdaten (z. B. Kautionsverwaltung)</li>
      <li>Kommunikationsdaten</li>
      <li>Bonitätsnachweise und Mieterauskunft</li>
    </ul>
    <h3>3. Zwecke und Rechtsgrundlagen</h3>
    <p>Die Daten werden erhoben und verarbeitet zur</p>
    <ul>
      <li>Verwaltung und Betreuung von Immobilien und Mietverhältnissen</li>
      <li>Erfüllung gesetzlicher Pflichten (Abrechnungen, Meldepflichten)</li>
      <li>Kommunikation mit Mietern, Eigentümern, Dienstleistern und Behörden</li>
      <li>Abwicklung von Schadens- und Versicherungsfällen</li>
    </ul>
    <p>Rechtsgrundlage ist insb. Art. 6 Abs. 1 lit. b, c, f DSGVO.</p>
    <h3>4. Datenweitergabe an Dritte</h3>
    <p>Übermittlungen erfolgen nur, soweit zur Vertragserfüllung (z. B. Handwerker, Banken, Steuerberater) oder zur Erfüllung gesetzlicher Pflichten erforderlich und zulässig. Keine Datenübertragung an Drittstaaten außerhalb der EU ohne eigene Einwilligung.</p>
    <h3>5. Speicherdauer</h3>
    <p>Ihre Daten werden nur so lange gespeichert, wie dies zur Abwicklung des jeweiligen Mietverhältnisses sowie zur Einhaltung gesetzlicher Aufbewahrungspflichten erforderlich ist.</p>
    <h3>6. Ihre Rechte</h3>
    <p>Sie haben das Recht auf Auskunft, Berichtigung, Löschung, Einschränkung der Verarbeitung, Datenübertragbarkeit sowie Widerspruch.<br>Kontaktieren Sie uns bei Fragen unter den angegebenen Kontaktdaten.</p>
    <h3>7. Änderungen</h3>
    <p>Diese Datenschutzerklärung kann bei rechtlichen Änderungen oder Anpassungen unseres Leistungsangebots aktualisiert werden.</p>
  </div>

  <div class="panel panel--paper fine">
    <h2>Sonderhonorare<br>(Beispiele, marktüblich)</h2>
    <ul>
      <li><b>Modernisierungs- oder Sanierungsbetreuung:</b> 80–120 € netto / Stunde oder alternativ 1–3% der Investitionssumme als pauschale Projektvergütung (insbesondere bei Großprojekten oder komplexen Bauphasen).</li>
      <li><b>Organisation und Moderation außerordentlicher Eigentümerversammlungen:</b> 250–500 € pauschal je Veranstaltung zzgl. Fahrt- und Materialkosten.</li>
      <li><b>Komplexe Versicherungsschadensabwicklung:</b> 80–120 € netto / Stunde.</li>
      <li><b>Gerichtliche und außergerichtliche Mahn- / Klageverfahren:</b> 80–120 € netto / Stunde bzw. nach RVG (bei bestimmten Tätigkeiten, z. B. Abwicklung von Räumungen).</li>
      <li><b>Erstellungs- und Übermittlungsgebühren für Einzelbescheinigungen (steuerlich, § 35a EStG):</b> 20–50 € pro Stück.</li>
    </ul>
    <div class="gap"></div>
    <h2 style="font-size:6.2px;margin-top:4px">Erweiterte Serviceleistungen (Beispiele)</h2>
    <ul>
      <li><b>Digitales Eigentümerportal:</b> Online-Zugriff auf Abrechnungen, Dokumente, Protokolle (monatlicher / jährlicher Pauschalbetrag z. B. 2–5 € je Einheit / Monat)</li>
      <li><b>Kommunikations- und Notfallmanagement (24 / 7):</b> Einrichtung einer Notfallhotline, schneller Service bei Schadensfällen (Pauschal- oder Aufwandsentschädigung)</li>
      <li><b>Regelmäßige Digital-Reporting- / Dashboards (Immobiliendaten, Leerstände, Rechnungsstatus):</b> Nach Vereinbarung, oft als Zusatzmodul oder Paketpreis</li>
      <li><b>Fördermittelberatung und -antrag, Energieberatung:</b> Pauschale oder 80–120 € netto / Stunde</li>
      <li><b>ESG-Dokumentation und Beratung:</b> z. B. Erstellung von Nachhaltigkeitsberichten, Beratung zu Fördermaßnahmen (nach Aufwand)</li>
      <li><b>Wartelistenmanagement und Bewerber-Screening:</b> z. B. Pauschalbetrag pro Vorgang/Mieter</li>
    </ul>
    <div class="contact">
      <b>Kontakt</b><br>Jonas Trewelt<br>info@wohnwerk-jt.de<br>Mobil: +49 1573 42 19 605<br>Am Lindenhang 7, 74921 Hohenweiler
    </div>
  </div>

  <div class="panel cover">
    <svg class="cover__photo" viewBox="0 0 160 340" role="img" aria-label="Foto: gläserne Hochhausfassaden von unten gesehen vor hellem Himmel">
      <defs>
        <linearGradient id="facade" x1="1" y1="0" x2="0" y2="1">
          <stop offset="0" stop-color="#27323a"/>
          <stop offset=".5" stop-color="#6f7d87"/>
          <stop offset="1" stop-color="#c9d2d8"/>
        </linearGradient>
      </defs>
      <polygon points="0,129 160,87 160,340 0,340" fill="url(#facade)"/>
    </svg>
    <div class="cover__title">
      <span>Haven Crest</span>
      <span>Property</span>
      <span>Stewardship</span>
    </div>
  </div>
</section>

<section class="spread spread--inside">
  <div class="panel panel--paper">
    <h2 style="font-size:8px;line-height:9.5px;margin-bottom:8px">Detailliertes Leistungsprofil<br>Haus- und Mietverwaltung</h2>
    <h3>1. Kaufmännische Verwaltung</h3>
    <ul>
      <li>Abschluss und Verwaltung sämtlicher Mietverträge (Erstellung, Überprüfung, Anpassung)</li>
      <li>Prüfung und Verbuchung von Mietzahlungen; Überwachung des Zahlungsverkehrs und Mahnwesen</li>
      <li>Verwaltung der Mietkautionen inkl. ordnungsgemäße Rückzahlung bei Auszug</li>
      <li>Laufende Buchhaltung, Budgetplanung und Abrechnung (u. a. Betriebskosten-, Heizkosten- und Jahresabrechnungen)</li>
      <li>Erstellung von Wirtschaftsplänen und Liquiditätsüberwachung</li>
      <li>Prüfung und Begleichung sämtlicher Bewirtschaftungskosten</li>
      <li>Erstellung von Reportings und Eigentümerberichten</li>
      <li>Unterstützung und Übernahme der steuerlichen Dokumentation (z. B. Bescheinigungen gem. § 35a EStG)</li>
    </ul>
    <h3>2. Technische Verwaltung &amp; Instandhaltung</h3>
    <ul>
      <li>Organisation und Kontrolle der laufenden Instandhaltung und sachgemäßen Instandsetzung</li>
      <li>Regelmäßige Objektbegehungen zur Überprüfung des Gebäudezustandes</li>
      <li>Einholung und Prüfung von Angeboten, Auftragsvergabe und Rechnungsbegleichung für Handwerker bzw. Dienstleister</li>
      <li>Kontrolle, Überwachung und Abnahme von Sanierungs- und Modernisierungsmaßnahmen</li>
      <li>Koordination und Management von Notfällen (z. B. Rohrbruch, Heizungsausfall) rund um die Uhr</li>
      <li>Sicherstellung der regelmäßigen Wartung technischer Anlagen und Überwachung gesetzlicher Fristen</li>
    </ul>
    <h3>3. Mieterbetreuung und Kommunikation</h3>
    <ul>
      <li>Auswahl und Bonitätsprüfung von Mietinteressenten, Durchführung von Besichtigungsterminen</li>
      <li>Abschluss und Anpassung von Mietverträgen, Übernahme von Wohnungsübergaben und -abnahmen inkl. Protokollierung</li>
      <li>Reaktion auf Anfragen, Bearbeitung von Beschwerden und Mängelanzeigen – auch mit Notfallmanagement</li>
      <li>Betreuung und Information der Mieter bei Modernisierungs-, Sanierungs- oder Reparaturmaßnahmen</li>
    </ul>
  </div>

  <div class="panel panel--paper">
    <ul>
      <li>Durchführung ordentlicher und außerordentlicher Mieterhöhungen (Staffelmiete, Indexmiete, Anpassung an Mietspiegel)</li>
      <li>Kündigungsmanagement und Hilfestellung beim Mieterwechsel</li>
    </ul>
    <h3>4. Behörden- und Versicherungsmanagement</h3>
    <ul>
      <li>Kommunikation mit städtischen Behörden zu Fragen von Abgaben, Genehmigungen, Sanierungen, Prüfungen oder Genehmigungen</li>
      <li>Abschluss und Verwaltung von Sach-, Gebäude-, Haftpflicht- und weiteren Versicherungen, Schadensmanagement mit Versicherungen</li>
      <li>Vertretung der Eigentümerinteressen gegenüber Behörden, Gerichten und Dritten</li>
    </ul>
    <h3>5. Zusatz- und Sonderleistungen (Beispiele)</h3>
    <ul>
      <li>Betreuung und Projektkoordination umfangreicher Modernisierungs-, Sanierungs- oder Umbaumaßnahmen</li>
      <li>Organisation, Durchführung und Moderation von Eigentümerversammlungen</li>
      <li>Erstellung besonderer Bescheinigungen, z. B. für steuerliche Zwecke</li>
      <li>Abwicklung von Versicherungsschäden mit erhöhter Komplexität</li>
      <li>Erledigung und Begleitung gerichtlicher oder außergerichtlicher Mahn- und Räumungsverfahren</li>
      <li>Organisation und Durchführung besonderer Dienstleistungsvergaben (z. B. Sondereinsätze Reinigungsfirmen, Hausmeisterdienste)</li>
      <li>Aufbau und Verwaltung von Wartelisten für Mietinteressenten</li>
      <li>Spezielle Beratungsleistungen z. B. im Rahmen von ESG- / Energieprojekten, Fördermittelanträgen oder Digitalisierung</li>
      <li>Vorbereitung und Durchführung von Eigentümerwechsel</li>
    </ul>
  </div>

  <div class="panel panel--slate">
    <h2 style="font-size:8px;line-height:9.5px;margin-bottom:1px">Mustervertrag für<br>Haus- und Mietverwaltung</h2>
    <h4 style="font-size:5px">Zwischen</h4>
    <p>[Name und Anschrift des Eigentümers / der Eigentümergemeinschaft]<br>(nachfolgend „Auftraggeber“ genannt)</p>
    <div class="gap"></div>
    <p>und<br>[Name und Anschrift der Verwaltung]</p>
    <div class="gap"></div>
    <p>(nachfolgend „Verwalter“ genannt)<br>wird folgender Haus- und Mietverwaltungsvertrag geschlossen:</p>
    <h3>§ 1 Vertragsgegenstand</h3>
    <ol>
      <li data-n="1.">Der Verwalter übernimmt die kaufmännische, technische und mietvertragliche Verwaltung der nachfolgend benannten Immobilie/n:</li>
      <li data-n="–">[Genaues Objekt / Adresse, ggf. Anzahl der Einheiten]</li>
      <li data-n="2.">Tätigkeitsbereiche, Umfang und Ausgestaltung richten sich nach diesem Vertrag und dem als Anlage beigefügten Leistungsprofil / Leistungsverzeichnis.</li>
      <li data-n="3.">Die Verwaltung umfasst sowohl das Gemeinschafts- bzw. Gesamteigentum als auch die Mietverwaltung der einzelnen Einheiten.</li>
    </ol>
    <h3>§ 2 Leistungsprofil des Verwalters</h3>
    <p>Das Leistungsprofil des Verwalters umfasst beispielhaft, jedoch nicht abschließend, folgende Tätigkeiten:</p>
    <h3>1. Kaufmännische Verwaltung</h3>
    <ul>
      <li>Abschluss, Verwaltung und Anpassung sämtlicher Mietverträge</li>
      <li>Erfassung, Überwachung und Auszahlung aller Mieten, Kautionen und sonstigen Zahlungen</li>
      <li>Mahnwesen, Bearbeitung von Zahlungsrückständen</li>
      <li>Laufende Buchhaltung, Erstellung von Abrechnungen / Betriebskosten / Jahresabrechnung</li>
      <li>Erstellung von Wirtschaftsplänen, Liquiditätsüberwachung</li>
      <li>Begleichung aller laufenden Bewirtschaftungskosten, Abwicklung von Steuer- und Abgabenzahlungen</li>
    </ul>
    <h3>2. Technische Verwaltung &amp; Instandhaltung</h3>
    <ul>
      <li>Regelmäßige Objektbegehungen und Erstellung technischer Berichte</li>
      <li>Vergabe, Kontrolle und Abnahme von Instandhaltungs-, Wartungs- und Reparaturarbeiten</li>
    </ul>
  </div>

  <div class="panel panel--slate">
    <ul>
      <li>Koordination und Überwachung von Modernisierungs- und Sanierungsmaßnahmen</li>
      <li>Sicherstellung der Einhaltung gesetzlicher Fristen (Prüfungen, Wartungen)</li>
      <li>Organisation der Beseitigung von Schäden und Notfällen (z. B. Wasser- / Brandschäden)</li>
    </ul>
    <h3>3. Mieterbetreuung und Kommunikation</h3>
    <ul>
      <li>Auswahl und Bonitätsprüfung von Mietinteressenten; Durchführung von Besichtigungen</li>
      <li>Abschluss, Anpassung und Kündigung von Mietverträgen</li>
      <li>Übergabe und Rücknahme von Wohnungen, Protokollierung des Zustands</li>
      <li>Beantwortung von Mieteranfragen und Beschwerden</li>
      <li>Durchführung von Mieterhöhungen; Kommunikation bei Modernisierungsmaßnahmen</li>
    </ul>
    <h3>4. Behörden- und Versicherungsmanagement</h3>
    <ul>
      <li>Kommunikation und Schriftwechsel mit Behörden (z. B. Einhaltung Meldepflichten, Anträge)</li>
      <li>Abschluss und Verwaltung von Gebäude- und Haftpflichtversicherungen</li>
      <li>Betreuung und Abwicklung von Versicherungsschäden</li>
    </ul>
    <h3>5. Zusatzleistungen / Sonderleistungen<br>(gegen gesondertes Honorar)</h3>
    <ul>
      <li>Betreuung und Projektverantwortung bei Modernisierungen / Sanierungen</li>
      <li>Erstellung steuerlicher / sonderrechtlicher Bescheinigungen</li>
      <li>Organisation, Vorbereitung und Durchführung von außerordentlichen Eigentümerversammlungen</li>
      <li>Bearbeitung und Begleitung von gerichtlichen oder außergerichtlichen Mahn- und Räumungsverfahren</li>
      <li>Verwaltung von Wartelisten für Mietinteressenten</li>
      <li>Sonderberatungen (z. B. ESG-Maßnahmen, Fördermittel, Digitalisierung)</li>
      <li>Organisation und Begleitung von Eigentümerwechseln</li>
      <li>Komplexe Abwicklung von Versicherungsschäden</li>
      <li>Weitere auf Anforderung individuell vereinbarte Leistungen</li>
    </ul>
    <h3>§ 3 Vergütung</h3>
    <ol>
      <li data-n="1.">Das monatliche Honorar für die Grundleistungen der Haus- und Mietverwaltung beträgt [z. B. 3–5% der Nettokaltmiete] je Einheit.</li>
      <li data-n="2.">Zusätzliche Dienstleistungen im Zusammenhang mit</li>
    </ol>
  </div>
</section>

</body>
</html>
```